Home Services- Spring Clean Options

Brightwell Crew provides a variety of Home Services- focused on cleaning & improving the exterior of the home:

 Power Washing- driveways, sidewalks, patios, decks, fence
 Fence Staining- make fence look new with variety of staining colors
 Gutter cleaning- important to make sure have proper Water Drainage
 Gutter Guard Installation- prevent damage to roof and house by keeping debris out of gutters and water flowing.
 Window Washing- our exterior washing team and reach the highest windows
 Landscape& Patio Lights- highlight areas for beauty and safety
Updates

We are are almost finished. Just please make sure you pay attention to the wording and grammer in Red thx

Target Market(s)

Middle to Upper level Home Owners (especially women)

Industry/Entity Type

Cleaning Services

Font styles to use
Serif
Sans Serif

Requirements
Must have
• Not be Cluttered- Clean friendly, professional look. Focus on the Professional

Info@GoBrightwellCrew.com
972-648-0000
Nice to have
• Pictures of services- these are just examples
Should not have
• Bigger and bolder Services & Specials. Want to Show all the Services we offer but do Not use too much detail- don't want it to look "cluttered"

```html
<!DOCTYPE html>
<html lang="en">
<head>
<meta charset="utf-8">
<title>Brightwell Crew – Home Services Flyer</title>
<link href="https://fonts.googleapis.com/css2?family=Tinos:wght@400;700&family=Open+Sans:wght@400;600;700;800&display=swap" rel="stylesheet">
<style>
  :root {
    --blue: #1d4f9e;
    --blue-dark: #163f80;
    --green: #3b9f3a;
    --paper: #ffffff;
    --panel: #eef1f5;
    --ink: #4a4f57;
    --photo-sky: #b9c6cf;
    --photo-wall: #6f7a80;
  }
  * { margin: 0; padding: 0; box-sizing: border-box; }
  html, body { width: 800px; height: 1200px; overflow: hidden; background: var(--paper); }
  .flyer {
    width: 800px; height: 1200px; display: flex; flex-direction: column;
    background: var(--paper); font-family: "Open Sans", sans-serif; color: var(--ink);
  }
  .brand {
    height: 110px; flex: none; display: flex; align-items: center; justify-content: center; gap: 12px;
  }
  .brand-dot { width: 26px; height: 26px; border-radius: 50%; background: var(--green); }
  .brand-name { font-size: 34px; font-weight: 800; color: var(--blue); letter-spacing: -0.5px; }
  .hero-photo {
    height: 400px; flex: none; margin: 0 28px;
    background: linear-gradient(160deg, var(--photo-sky) 0%, #9aa7ae 40%, var(--photo-wall) 100%);
  }
  .headline-band {
    flex: none; height: 140px; background: var(--blue); color: #fff; text-align: center;
    padding: 16px 20px 0; font-family: "Tinos", serif;
  }
  .headline-title { font-size: 44px; font-weight: 400; letter-spacing: 1px; line-height: 1.1; }
  .headline-sub { font-size: 31px; line-height: 1.2; margin-top: 4px; }
  .services {
    position: relative; flex: 1; background: var(--panel); padding: 46px 60px 0;
  }
  .services-tab {
    position: absolute; top: -18px; left: 50%; transform: translateX(-50%);
    background: var(--green); color: #fff; font-weight: 700; font-size: 17px;
    letter-spacing: 1px; padding: 7px 34px; white-space: nowrap;
  }
  .service-grid {
    display: grid; grid-template-columns: repeat(3, 200px); column-gap: 40px; row-gap: 20px;
  }
  .service-card { text-align: center; }
  .service-photo { height: 105px; }
  .service-title {
    color: var(--green); font-weight: 700; font-size: 11.5px; letter-spacing: 0.5px;
    line-height: 1.3; margin-top: 8px; text-transform: uppercase;
  }
  .service-text { font-size: 10px; line-height: 1.35; margin-top: 3px; padding: 0 10px; }
  .contact-bar {
    flex: none; height: 75px; background: var(--blue-dark); color: #fff;
    display: flex; align-items: center; justify-content: space-between; padding: 0 40px;
  }
  .contact-item { display: flex; align-items: center; gap: 8px; font-size: 13px; }
  .contact-phone { font-size: 24px; font-weight: 700; }
  .contact-item svg { flex: none; }
</style>
</head>
<body>
<div class="flyer">
  <header class="brand">
    <span class="brand-dot"></span>
    <span class="brand-name">Brightwell Crew</span>
  </header>

  <div class="hero-photo" role="img" aria-label="Photo of a worker in a blue shirt power washing the siding of a house"></div>

  <section class="headline-band">
    <h1 class="headline-title">HOME SERVICES</h1>
    <p class="headline-sub">Cleaning &amp; Improving the exterior of the home</p>
  </section>

  <section class="services">
    <div class="services-tab">OUR SERVICES</div>
    <div class="service-grid">
      <article class="service-card">
        <div class="service-photo" role="img" aria-label="Photo of a driveway being power washed" style="background:linear-gradient(135deg,#8e9499,#c9cdd0)"></div>
        <h2 class="service-title">Power Washing</h2>
        <p class="service-text">Driveways, sidewalks, patios, decks, fence</p>
      </article>
      <article class="service-card">
        <div class="service-photo" role="img" aria-label="Photo of a wooden fence being stained" style="background:linear-gradient(135deg,#7a4a2c,#b77a4b)"></div>
        <h2 class="service-title">Fence Staining</h2>
        <p class="service-text">Make fence look new with variety of staining colors</p>
      </article>
      <article class="service-card">
        <div class="service-photo" role="img" aria-label="Photo of a gutter being cleaned of leaves" style="background:linear-gradient(135deg,#6b6a3a,#a89a5c)"></div>
        <h2 class="service-title">Gutter Cleaning</h2>
        <p class="service-text">Important to make sure you have proper water drainage</p>
      </article>
      <article class="service-card">
        <div class="service-photo" role="img" aria-label="Photo of a gutter guard installed on a roof edge" style="background:linear-gradient(135deg,#5d5450,#a29a93)"></div>
        <h2 class="service-title">Gutter Guard<br>Installation</h2>
        <p class="service-text">Prevent damage to roof and house by keeping debris out of gutters</p>
      </article>
      <article class="service-card">
        <div class="service-photo" role="img" aria-label="Photo of exterior windows being washed" style="background:linear-gradient(135deg,#8fb1c9,#d8e3ea)"></div>
        <h2 class="service-title">Window Washing</h2>
        <p class="service-text">Our exterior washing team can reach the highest windows</p>
      </article>
      <article class="service-card">
        <div class="service-photo" role="img" aria-label="Photo of a patio lit by landscape lights at dusk" style="background:linear-gradient(135deg,#2e2a1c,#b8862f)"></div>
        <h2 class="service-title">Landscape &amp;<br>Patio Lights</h2>
        <p class="service-text">Highlight areas for beauty and safety</p>
      </article>
    </div>
  </section>

  <footer class="contact-bar">
    <div class="contact-item">
      <svg width="24" height="24" viewBox="0 0 24 24" aria-hidden="true"><path fill="#fff" d="M6.6 10.8a15.1 15.1 0 0 0 6.6 6.6l2.2-2.2a1 1 0 0 1 1-.25 11.4 11.4 0 0 0 3.6.57 1 1 0 0 1 1 1V20a1 1 0 0 1-1 1A17 17 0 0 1 3 4a1 1 0 0 1 1-1h3.5a1 1 0 0 1 1 1c0 1.25.2 2.45.57 3.57a1 1 0 0 1-.25 1z"/></svg>
      <span class="contact-phone">972-648-0000</span>
    </div>
    <div class="contact-item">
      <svg width="18" height="18" viewBox="0 0 24 24" aria-hidden="true"><g fill="none" stroke="#fff" stroke-width="2"><circle cx="12" cy="12" r="10"/><path d="M2 12h20M12 2c3 3 3 17 0 20M12 2c-3 3-3 17 0 20"/></g></svg>
      <span>www.brightwellcrew.com</span>
    </div>
    <div class="contact-item">
      <svg width="18" height="18" viewBox="0 0 24 24" aria-hidden="true"><g fill="none" stroke="#fff" stroke-width="2"><rect x="2" y="5" width="20" height="14" rx="1"/><path d="M2 6l10 7 10-7"/></g></svg>
      <span>Info@GoBrightwellCrew.com</span>
    </div>
  </footer>
</div>
</body>
</html>
```